DESIGN A LEAFLET FOR A CANNABIS CLUB!!

We need a leaflet design for a cannabis club based in the United Kingdom, called Silver Pond Cannabis Club

PLEASE, FEEL FREE TO ADD YOUR OWN INFO ETC

Just want attention drawn to the INSTAGRAM/WEBSITE whilst looking semi-professional

LEGALIZE IT (title)

Government officials are denying your right to access legal Cannabis.

Over Thirty-five countries already have legal access in one form or another... What are we waiting for ?

I'd ideally like the leaflet to be A6 size

"INSTAGRAM LOGO": Silverpondcannabisclub
*MUST SEE*
"FACEBOOK LOGO": Silverpondcannabisclub
WEB: www.silverpondcannabisclub-example.com

Check us out!
*Cannabis Discussion Forum*
*Weed related news*
*Awesome Documentaries*

Industry/Entity Type

Club

Requirements
Must have
• Please use my logo on leaflet somewhere, feel free to re-size it
• Back of leaflet to just have my cannabis logo in large with green and smoky background
Nice to have
• PLEASE, FEEL FREE TO ADD YOUR OWN INFO ETC
• Just want attention drawn to INSTAGRAM/WEBSITE whilst looking semi-professional
Should not have
• Plain, boring, minimal effort

```html
<!DOCTYPE html>
<html lang="en">
<head>
<meta charset="utf-8">
<title>Silver Pond Cannabis Club – Leaflet</title>
<link rel="stylesheet" href="https://fonts.googleapis.com/css2?family=Oswald:wght@400;500;600;700&display=swap">
<style>
  :root{
    --stage:#eceeec;
    --leaf-green:#1f9a2c;
    --leaf-green-dark:#137a1f;
    --fresh-top:#7fd36e;
    --fresh-mid:#c9eec0;
    --paper:#ffffff;
    --body-brown:#5b4a36;
    --name-brown:#7a4219;
    --back-green:#3db833;
    --back-green-deep:#2a9a24;
    --icon-dark:#4a4a4a;
    --white:#ffffff;
  }
  *{box-sizing:border-box;margin:0;padding:0}
  html,body{width:1200px;height:719px;overflow:hidden}
  body{background:var(--stage);position:relative;font-family:"Oswald",sans-serif}

  .leaflet{position:absolute;box-shadow:0 10px 24px rgba(0,0,0,.28);overflow:hidden}

  /* Front */
  .leaflet--front{left:40px;top:34px;width:440px;height:650px;background:var(--paper)}
  .front__sky{position:absolute;left:0;top:0;width:440px;height:520px}
  .front__title{position:absolute;left:0;right:0;top:22px;text-align:center;font-weight:700;font-size:66px;letter-spacing:2px;color:var(--leaf-green);line-height:1}
  .front__copy{position:absolute;left:46px;right:30px;top:114px;color:var(--body-brown);font-weight:500;font-size:20px;line-height:1.3}
  .front__copy p+p{margin-top:10px}
  .front__features{position:absolute;left:46px;right:20px;top:276px;color:var(--body-brown);font-size:17px;line-height:1.45;font-weight:400;white-space:nowrap}
  .front__cta{color:var(--leaf-green);font-weight:700;font-size:23px;margin-right:10px}
  .contact-list{position:absolute;list-style:none}
  .contact-list li{display:flex;align-items:center;gap:10px;height:30px;font-weight:600;font-size:15px;letter-spacing:0;white-space:nowrap}
  .contact-list .icon{width:20px;height:20px;background:var(--icon-dark);border-radius:4px;flex:none}
  .contact-list .icon--web{border-radius:50%}
  .front__contacts{left:64px;top:342px;color:var(--leaf-green)}
  .front__logo{position:absolute;left:40px;top:520px;display:flex;align-items:center;gap:16px}
  .mascot{background:radial-gradient(circle at 50% 45%,#8fe05a,#3fb52a 65%,#2a8f1e);border-radius:50%}
  .front__mascot{width:118px;height:118px}
  .club-name{color:var(--name-brown);font-weight:600;line-height:1.05}
  .front__name{font-size:34px;width:230px}

  /* Back */
  .leaflet--back{left:520px;top:118px;width:640px;height:470px;
    background:
      radial-gradient(circle at 20% 30%,rgba(255,255,255,.18) 0 60px,transparent 61px),
      radial-gradient(circle at 85% 20%,rgba(255,255,255,.14) 0 50px,transparent 51px),
      radial-gradient(circle at 70% 80%,rgba(255,255,255,.12) 0 70px,transparent 71px),
      linear-gradient(160deg,var(--back-green) 0%,var(--back-green-deep) 100%)}
  .back__logo{position:absolute;left:50px;top:60px;display:flex;align-items:center;gap:24px}
  .back__mascot{width:190px;height:190px}
  .back__name{font-size:50px;width:330px;color:var(--white)}
  .back__contacts{left:180px;top:325px;color:var(--white)}
  .back__contacts .icon{background:var(--white)}
</style>
</head>
<body>

<section class="leaflet leaflet--front" aria-label="Leaflet front">
  <svg class="front__sky" viewBox="0 0 440 520" aria-hidden="true">
    <defs>
      <linearGradient id="sky" x1="0" y1="0" x2="0" y2="1">
        <stop offset="0" stop-color="var(--fresh-top)"/>
        <stop offset=".55" stop-color="var(--fresh-mid)"/>
        <stop offset="1" stop-color="#eefaea"/>
      </linearGradient>
    </defs>
    <path d="M0 0H440V440Q220 520 0 440Z" fill="url(#sky)"/>
    <path d="M0 440Q220 520 440 440V452Q220 532 0 452Z" fill="var(--leaf-green)" opacity=".55"/>
  </svg>

  <h1 class="front__title">LEGALIZE IT</h1>
  <div class="front__copy">
    <p>Government officials are denying your right to access legal Cannabis.</p>
    <p>Over Thirty-five countries already have legal access in one form or another... What are we waiting for?</p>
  </div>
  <p class="front__features"><span class="front__cta">CHECK US OUT!</span>* Cannabis Discussion Forum<br>* Weed related news * Awesome Documentaries</p>

  <ul class="contact-list front__contacts">
    <li><span class="icon"></span>SILVERPONDCANNABISCLUB</li>
    <li><span class="icon"></span>SILVERPONDCANNABISCLUB</li>
    <li><span class="icon icon--web"></span>WWW.SILVERPONDCANNABISCLUB-EXAMPLE.COM</li>
  </ul>

  <div class="front__logo">
    <div class="mascot front__mascot" role="img" aria-label="Club mascot illustration: smiling cartoon cannabis leaf holding a pipe"></div>
    <p class="club-name front__name">Silver Pond Cannabis Club</p>
  </div>
</section>

<section class="leaflet leaflet--back" aria-label="Leaflet back">
  <div class="back__logo">
    <div class="mascot back__mascot" role="img" aria-label="Club mascot illustration: smiling cartoon cannabis leaf holding a pipe"></div>
    <p class="club-name back__name">Silver Pond Cannabis Club</p>
  </div>
  <ul class="contact-list back__contacts">
    <li><span class="icon"></span>SILVERPONDCANNABISCLUB</li>
    <li><span class="icon"></span>SILVERPONDCANNABISCLUB</li>
    <li><span class="icon icon--web"></span>WWW.SILVERPONDCANNABISCLUB-EXAMPLE.COM</li>
  </ul>
</section>

</body>
</html>
```